Kolna Thai Massage Double Sided Flyer Luxury

I require a double sided flyer
we are a Thai Massage Spa
Would like gold, deep purple and bronze colours
Something eye catching and looks professional

```html
<!DOCTYPE html>
<html lang="en">
<head>
<meta charset="utf-8">
<title>Kolna Thai Massage – Flyer</title>
<link rel="stylesheet" href="https://fonts.googleapis.com/css2?family=Marcellus&family=Josefin+Sans:ital,wght@0,300;0,400;1,300&family=Pinyon+Script&display=swap">
<style>
  :root {
    --plum-deep: #1e1129;
    --plum-mid: #311b44;
    --plum-low: #241631;
    --gold: #e6c25e;
    --gold-soft: #c9a24e;
    --bronze: #8c7048;
    --divider: #2a1a36;
  }
  * { margin: 0; padding: 0; box-sizing: border-box; }
  html, body { width: 1200px; height: 855px; overflow: hidden; background: var(--plum-deep); }
  .flyer { position: relative; width: 1200px; height: 855px; overflow: hidden; }

  .panel { position: absolute; top: 0; height: 855px; }
  .panel--front { left: 0; width: 605px; }
  .panel--back { left: 605px; width: 595px; border-left: 1px solid var(--divider); }

  .pattern-field { position: absolute; inset: 0; background: var(--plum-deep); }
  .front-bands { position: absolute; inset: 0; }

  .brand-block {
    position: absolute; left: 0; width: 605px; top: 262px;
    display: flex; justify-content: center; align-items: center; gap: 12px;
  }
  .brand-block__square { width: 12px; height: 12px; background: var(--gold); }
  .brand-block__name {
    font-family: "Marcellus", serif; font-size: 24px; letter-spacing: 3px;
    color: var(--gold);
  }

  .front-name {
    position: absolute; left: 0; width: 605px; top: 536px; text-align: center;
    font-family: "Marcellus", serif; color: var(--gold); line-height: 1;
  }
  .front-name__line1 { font-size: 17px; letter-spacing: 3px; }
  .front-name__line2 { font-size: 13.5px; letter-spacing: 2.5px; margin-top: 4px; }

  .back-content { position: absolute; inset: 0; text-align: center; color: var(--gold-soft); }
  .back-content > * { position: absolute; left: 0; width: 595px; }

  .welcome { top: 48px; font-family: "Pinyon Script", cursive; font-size: 20px; color: var(--gold); }
  .headline {
    font-family: "Marcellus", serif; color: var(--gold); line-height: 1;
  }
  .headline--luxury { top: 73px; font-size: 34px; letter-spacing: 3px; }
  .headline--massages { top: 282px; font-size: 33px; letter-spacing: 5px; }

  .copy {
    font-family: "Josefin Sans", sans-serif; font-weight: 300;
    font-size: 11.2px; letter-spacing: 1.4px; line-height: 20.5px; text-transform: uppercase;
    padding: 0 22px;
  }
  .copy--intro-1 { top: 116px; }
  .copy--intro-2 { top: 184px; }
  .copy--massages { top: 331px; }

  .treatment {
    font-family: "Marcellus", serif; color: var(--gold); font-size: 19px; letter-spacing: 3px; line-height: 1;
  }
  .treatment--deep { top: 416px; }
  .treatment--floor { top: 568px; }

  .price-row {
    font-family: "Josefin Sans", sans-serif; font-weight: 400; color: var(--gold);
    font-size: 15px; letter-spacing: 2px; line-height: 1;
    display: flex; justify-content: center; gap: 26px;
  }
  .price-row b { font-weight: 400; }
  .price-row--deep60 { top: 452px; }
  .price-row--deep90 { top: 503px; }
  .price-row--floor60 { top: 601px; }

  .note {
    font-family: "Josefin Sans", sans-serif; font-weight: 300; color: var(--gold-soft);
    font-size: 11.5px; letter-spacing: 1.6px; line-height: 20.5px;
  }
  .note--deep60 { top: 470px; }
  .note--deep90 { top: 521px; }
  .note--floor60 { top: 621px; }

  .vouchers {
    top: 674px; font-family: "Josefin Sans", sans-serif; font-style: italic; font-weight: 300;
    font-size: 10px; letter-spacing: 1.4px; color: var(--bronze);
  }

  .address {
    top: 726px; font-family: "Josefin Sans", sans-serif; font-weight: 300;
    font-size: 12.2px; letter-spacing: 1.6px; line-height: 18.4px; color: var(--bronze);
  }
  .address a {
    display: block; margin-top: 3px; color: var(--gold-soft); font-style: italic;
    text-decoration: none; font-size: 12px;
  }
</style>
</head>
<body>
<main class="flyer">

  <section class="panel panel--front">
    <div class="pattern-field" role="img" aria-label="Fine gold Thai floral line pattern on deep purple"></div>
    <svg class="front-bands" width="605" height="855" viewBox="0 0 605 855" aria-hidden="true">
      <defs>
        <linearGradient id="bandFill" x1="0" y1="0" x2="0" y2="1">
          <stop offset="0" stop-color="#341d48"/>
          <stop offset="1" stop-color="#231530"/>
        </linearGradient>
      </defs>
      <polygon points="0,521 304,669 605,524 605,855 0,855" fill="url(#bandFill)"/>
      <line x1="0" y1="521" x2="304" y2="669" stroke="#e6c25e" stroke-width="2.4"/>
      <line x1="0" y1="819" x2="605" y2="524" stroke="#e6c25e" stroke-width="2.4"/>
    </svg>

    <div class="brand-block">
      <span class="brand-block__square"></span>
      <span class="brand-block__name">KOLNA THAI MASSAGE</span>
    </div>

    <div class="front-name">
      <div class="front-name__line1">KOLNA THAI</div>
      <div class="front-name__line2">MASSAGE</div>
    </div>
  </section>

  <section class="panel panel--back">
    <div class="pattern-field" role="img" aria-label="Faint Thai floral line pattern on deep purple"></div>
    <div class="back-content">
      <p class="welcome">Welcome to</p>
      <h1 class="headline headline--luxury">LUXURY</h1>
      <p class="copy copy--intro-1">Set in the heart of Elmdale, Kolna Thai Massage will allow you to immerse yourself in a place where your wellbeing and rejuvination is at the centre of what we do.</p>
      <p class="copy copy--intro-2">Using Thai traditions, our highly trained therapists offer reevitalising body treatments with their deep tissue massage techniques. In their hands, you will see and feel immediate results.</p>

      <h2 class="headline headline--massages">MASSAGES</h2>
      <p class="copy copy--massages">Restore balance. Revive your senses. Discover all the ways Kolna Thai massage can breathe new life into your body and soul.</p>

      <h3 class="treatment treatment--deep">DEEP TISSUE MASSAGE</h3>
      <p class="price-row price-row--deep60"><span>60 MINUTES</span><b>£45</b></p>
      <p class="note note--deep60">OIL MASSAGE PERSONALISED, LIGHT TO FIRM PRESSURE</p>
      <p class="price-row price-row--deep90"><span>90 MINUTES</span><b>£55</b></p>
      <p class="note note--deep90">OIL MASSAGE, LIGHT TO FIRM PRESSURE</p>

      <h3 class="treatment treatment--floor">THAI FLOOR TRADITIONAL MASSAGE</h3>
      <p class="price-row price-row--floor60"><span>60 MINUTES</span><b>£45</b></p>
      <p class="note note--floor60">DRY MASSAGE, MEDIUM TO FIRM PRESSURE APPLYING<br>STRETCHING TECHNIQUES</p>

      <p class="vouchers">GIFT VOUCHERS AVAILIBLE</p>

      <address class="address">
        KOLNA THAI MASSAGE<br>
        42 ORCHARD ROW<br>
        BRACKFORD<br>
        BK4 2QT<br>
        01134960218
        <a href="#">WWW.KOLNATHAIMASSAGE.CO.UK</a>
      </address>
    </div>
  </section>

</main>
</body>
</html>
```